Business Card for Pottery and Jewellery Designer

A new business card design is needed to accompany a newly launching pottery and jewellery website. The company logo has been attached for use. The company is called Glazewick Studio. For a sense of the vibe please see the website (it is currently under construction but this way you'll get a feel for the style) www.GlazewickStudio.com

The website font is Pontano Sans for the body of the text with Overlock for headers.

The overall look should be clean and elegant. The back side can have just the logo. The front side should have a smaller logo and the following details displayed:

Glazewick Studio
Designer: Hollis Marrow
Phone: xxx.xxx.xxxx
Email: Designer@GlazewickStudio.com

The structure of displaying this is completely up to you. Different layouts and creative methods of displaying contact info are welcome as long as it stays clean/uncluttered.

No product photographs are to be included in the design as the catalogue changes quickly.

Colour preferences lean towards elegant and understated (charcoal grey, dark navy blue etc.)

Please let me know if you have any further questions or further details required.

Target Market(s)

Target market is 30+ year old women

Industry/Entity Type

Construction

Colors
ffffff
1b1b1b
474747
d9d9d9
fafafa
0355a3

Requirements
Must have
• The submissions so far have looked very typical and don't stand out right now. They're also all in navy with very little variation. I'm looking for something that stands out a it more while still being clean-looking.
Nice to have
• I've attached a few design samples and an idea for a backdrop. It would be great to see some designs in black, white, and grey with only a hint of color.
Should not have
• Product Images

```html
<!DOCTYPE html>
<html lang="en">
<head>
<meta charset="utf-8">
<title>Glazewick Studio — Business Card</title>
<link href="https://fonts.googleapis.com/css2?family=Pontano+Sans&display=swap" rel="stylesheet">
<style>
  :root {
    --charcoal: #1b1b1b;
    --graphite: #474747;
    --silver: #d9d9d9;
    --paper: #ffffff;
    --paper-soft: #fafafa;
    --accent: #0355a3;
    --backdrop: #ececec;
  }
  * { margin: 0; padding: 0; box-sizing: border-box; }
  html, body {
    width: 1200px; height: 1000px; overflow: hidden;
    background: var(--backdrop);
    font-family: "Pontano Sans", sans-serif;
  }
  .canvas { position: relative; width: 1200px; height: 1000px; }

  .card {
    position: absolute; left: 320px;
    width: 560px; height: 320px;
    overflow: hidden;
    box-shadow: 0 6px 22px rgba(0,0,0,0.16);
  }

  .brand {
    display: flex; align-items: center; gap: 14px;
    color: var(--charcoal);
    text-transform: uppercase;
    letter-spacing: 1px;
    white-space: nowrap;
  }
  .brand-dot {
    border-radius: 50%;
    background: var(--accent);
    flex: none;
  }

  /* Back side */
  .card-back {
    top: 130px;
    background: radial-gradient(ellipse at 50% 45%, var(--paper) 0%, var(--paper-soft) 40%, var(--silver) 100%);
    display: flex; align-items: center; justify-content: center;
  }
  .card-back .brand { font-size: 34px; }
  .card-back .brand-dot { width: 28px; height: 28px; }

  /* Front side */
  .card-front { top: 550px; background: var(--paper); }
  .front-bands { position: absolute; inset: 0; width: 100%; height: 100%; }
  .front-content {
    position: absolute; inset: 0;
    display: flex; flex-direction: column; align-items: center;
    padding-top: 78px;
  }
  .card-front .brand { font-size: 24px; margin-bottom: 22px; }
  .card-front .brand-dot { width: 18px; height: 18px; }
  .designer { color: var(--graphite); font-size: 18px; margin-bottom: 24px; }
  .contact {
    list-style: none; text-align: center;
    color: var(--graphite); font-size: 13px; line-height: 1.7;
  }
</style>
</head>
<body>
<main class="canvas">

  <section class="card card-back" aria-label="Card back">
    <div class="brand">
      <span class="brand-dot"></span>
      <span class="brand-name">Glazewick Studio</span>
    </div>
  </section>

  <section class="card card-front" aria-label="Card front">
    <svg class="front-bands" viewBox="0 0 560 320" preserveAspectRatio="none" aria-hidden="true">
      <defs>
        <linearGradient id="charcoalFade" x1="0" y1="0" x2="0" y2="1">
          <stop offset="0" stop-color="#1b1b1b"/>
          <stop offset="1" stop-color="#474747"/>
        </linearGradient>
      </defs>
      <path d="M0,0 H560 V70 C470,28 330,14 120,26 C70,28 30,20 0,10 Z" fill="url(#charcoalFade)"/>
      <path d="M0,30 C90,40 200,34 330,30 C430,28 510,40 560,70 V74 C500,44 420,34 330,36 C200,40 90,46 0,36 Z" fill="#0355a3"/>
      <path d="M0,290 C110,270 260,262 400,280 C470,290 520,300 560,300 V320 H0 Z" fill="url(#charcoalFade)"/>
      <path d="M0,282 C120,262 270,254 410,272 C480,281 530,292 560,292 V296 C520,294 470,284 400,276 C260,258 110,266 0,286 Z" fill="#d9d9d9"/>
    </svg>
    <div class="front-content">
      <div class="brand">
        <span class="brand-dot"></span>
        <span class="brand-name">Glazewick Studio</span>
      </div>
      <p class="designer">Designer: Hollis Marrow</p>
      <ul class="contact">
        <li>Phone: xxx.xxx.xxxx</li>
        <li>Email: Designer@GlazewickStudio.com</li>
      </ul>
    </div>
  </section>

</main>
</body>
</html>
```